Cover for a Non-Fiction Book on Authoritarianism for a Washington D.C. Think Tank

Create a dynamic and engaging cover highlighting the role of contemporary and historical authoritarianism for a non-fiction edited volume. The book brings together chapters from many leading academics on the subject. The tone should be serious but provocative. Proprietary images are not acceptable as we are not budgeting for licensing. The books dimensions are 6x9. Preference will be given to designers with front and back cover design with sample ipsum lorum text.

One of covers that we particularly liked was "How Quiet Defiance Endures" a link to the image on shelvoria is: http://www.shelvoria-books.example/s/ref=nb_sb_noss/482-7715093-6620841?url=search-alias%3Daps&field-keywords=How+Quiet+Defiance+Endures

Attached is a draft version of the manuscript to assist in shaping your creative vision.

Project Deadline Extended Reason: I have extended the deadline at the request of the editors. They would like to see some designs that rely less heavily on the themes of fists and barbed wire to reference authoritarianism. I apologize to designs with current submissions, some of them are very professional, however none of the designs are currently under consideration for use. Added Saturday, January 24, 2015

Project Deadline Extended Reason: Editors are still unsatisfied with current sample of options. I apologize to those current contributors, but anything challenging and new would be well received. Added Friday, January 30, 2015

Project Deadline Extended Reason: I've updated the deadline so that designers that were well ranked can submit full front and back covers to assist the book editors in making their final decision. Added Friday, February 13, 2015

Font styles to use
Serif
Sans Serif

Requirements
Must have
• 1) Title: Are Strongmen Regaining the Upper Ground
• 2) Editors: Tobias Lindqvern and Elena K. Marwood
• 3) Language from client: "a simple design that captured both a symbol of repression and resistance would be ideal. The cover of How Quiet Defiance Endures is a great example. Nothing busy or overly complicated. The image of mass street protests may be overused at this point so I'd opt for something a bit more creative. Vibrant colors always great."
• 4) This final project design must use the attached InDesign template file when constructing the cover (IDML and INDD versions of the template are available).
Nice to have
• Feel free to use Harborline Forum logo designs pulled from the web.
Should not have
• Photographs that would require compensating a copyright holder.

```html
<!DOCTYPE html>
<html lang="en">
<head>
<meta charset="utf-8">
<title>Are Strongmen Regaining the Upper Ground — Cover</title>
<link rel="stylesheet" href="https://fonts.googleapis.com/css2?family=Bebas+Neue&family=Oswald:wght@500;600;700&display=swap">
<style>
  :root {
    --canvas: #e6e6e6;
    --paper: #f4f4f4;
    --ink: #111111;
    --red: #d9262b;
    --red-deep: #7e1518;
    --white: #ffffff;
    --grey-text: #222222;
    --logo-blue: #1f3f7a;
  }
  * { box-sizing: border-box; margin: 0; padding: 0; }
  html, body {
    width: 1200px; height: 800px; overflow: hidden;
    background: var(--canvas);
  }
  .spread {
    position: absolute; left: 170px; top: 100px;
    display: flex; height: 600px;
    box-shadow: 0 10px 30px rgba(0,0,0,.12);
  }
  .back-cover, .front-cover, .spine {
    position: relative; height: 600px; background: var(--paper);
  }
  .back-cover, .front-cover { width: 400px; }

  /* Back cover */
  .back-cover { padding: 26px 34px 0 34px; }
  .back-authors {
    font-family: "Oswald", sans-serif; font-weight: 600;
    font-size: 11px; text-transform: uppercase; text-align: right;
    color: var(--ink); letter-spacing: .2px;
  }
  .back-title {
    font-family: "Bebas Neue", sans-serif; font-weight: 400;
    font-size: 31px; line-height: 1; color: var(--ink);
    margin-top: 14px; letter-spacing: .3px; white-space: nowrap;
  }
  .back-title .accent { color: var(--red); }
  .back-blurb {
    font-family: "Oswald", sans-serif; font-weight: 600;
    font-size: 10.3px; line-height: 1.28; color: var(--grey-text);
    text-align: justify; margin-top: 16px;
  }
  .back-footer {
    position: absolute; left: 34px; right: 34px; bottom: 26px;
    display: flex; justify-content: space-between; align-items: flex-end;
  }
  .publisher {
    display: flex; align-items: center; gap: 6px;
    font-family: "Oswald", sans-serif; font-weight: 600; font-size: 12px;
    color: var(--logo-blue); margin-bottom: 30px;
  }
  .publisher-dot {
    width: 12px; height: 12px; border-radius: 50%; background: var(--logo-blue);
  }
  .isbn-box {
    width: 118px; height: 58px; background: var(--ink); color: var(--white);
    display: flex; align-items: center; justify-content: center;
    font-family: "Oswald", sans-serif; font-weight: 600; font-size: 13px;
  }

  /* Spine */
  .spine {
    width: 40px; border-left: 1px solid #d6d6d6; border-right: 1px solid #d6d6d6;
    display: flex; align-items: center; flex-direction: column;
    padding-top: 20px;
  }
  .spine-title {
    writing-mode: vertical-rl;
    font-family: "Bebas Neue", sans-serif; font-size: 26px;
    color: var(--ink); letter-spacing: .5px; line-height: 1; white-space: nowrap;
  }
  .spine-title .accent { color: var(--red); }

  /* Front cover */
  .front-cover { padding: 34px 24px 0 24px; }
  .front-frame {
    border: 6px solid var(--ink); height: 468px; position: relative;
    background: var(--ink); display: flex; flex-direction: column;
  }
  .front-artwork {
    flex: 1;
    background: linear-gradient(180deg, var(--red) 0%, var(--red-deep) 55%, var(--ink) 100%);
  }
  .front-title {
    font-family: "Bebas Neue", sans-serif; font-weight: 400; color: var(--white);
    padding: 8px 12px 12px 12px; line-height: 1; letter-spacing: .3px;
    white-space: nowrap;
  }
  .front-title .line-one { font-size: 44px; display: block; }
  .front-title .line-two { font-size: 29px; display: block; }
  .front-title .accent { color: var(--red); }
  .front-authors {
    margin-top: 12px;
    display: flex; align-items: center; justify-content: center; gap: 10px;
    font-family: "Oswald", sans-serif; font-weight: 700; font-size: 14px;
    text-transform: uppercase; color: var(--ink); letter-spacing: .3px;
  }
  .front-authors svg { width: 13px; height: 13px; }
  .front-rule {
    height: 3px; background: var(--ink); margin-top: 6px;
  }
</style>
</head>
<body>
  <div class="spread">
    <section class="back-cover">
      <p class="back-authors">Tobias Lindqvern and Elena K. Marwood</p>
      <h2 class="back-title">Are <span class="accent">Strongmen</span><br>Regaining the Upper Ground</h2>
      <p class="back-blurb">Lorem ipsum dolor sit amet, consectetur adipisicing elit, sed do eiusmod tempor incididunt ut labore et dolore magna aliqua. Ut enim ad minim veniam, quis nostrud exercitation. Lorem ipsum dolor sit amet, consectetur adipisicing elit, sed do eiusmod tempor incididunt ut labore et dolore magna aliqua. Ut enim ad minim veniam, quis nostrud exercitation. Lorem ipsum dolor sit amet, consectetur adipisicing elit, sed do eiusmod tempor incididunt ut labore et dolore magna aliqua. Ut enim ad minim veniam, quis nostrud exercitation. Lorem ipsum dolor sit amet, consectetur adipisicing elit, sed do eiusmod tempor incididunt ut labore et dolore magna aliqua. Ut enim ad minim veniam, quis nostrud exercitation. Lorem ipsum dolor sit amet, consectetur adipisicing elit, sed do eiusmod tempor incididunt ut labore et dolore magna aliqua. Ut enim ad minim veniam, quis nostrud exercitation. Lorem ipsum dolor sit amet, consectetur adipisicing elit, sed do eiusmod tempor incididunt ut labore et dolore magna aliqua. Ut enim ad minim veniam, quis nostrud exercitation. Lorem ipsum dolor sit amet, consectetur adipisicing elit, sed do eiusmod tempor incididunt ut labore et dolore magna aliqua. Ut enim ad minim veniam, quis nostrud exercitation.</p>
      <div class="back-footer">
        <div class="publisher"><span class="publisher-dot"></span><span>Harborline Forum</span></div>
        <div class="isbn-box">ISBN</div>
      </div>
    </section>

    <section class="spine">
      <p class="spine-title">Are <span class="accent">Strongmen</span> Regaining the Upper Ground</p>
    </section>

    <section class="front-cover">
      <div class="front-frame">
        <div class="front-artwork" role="img" aria-label="Cover illustration: raised black fist over red and white rays and a city skyline silhouette"></div>
        <h1 class="front-title">
          <span class="line-one">Are <span class="accent">Strongmen</span></span>
          <span class="line-two">Regaining the Upper Ground</span>
        </h1>
      </div>
      <div class="front-authors">
        <svg viewBox="0 0 24 24" aria-hidden="true"><polygon fill="#d9262b" points="12,1 15,9 23,9 16.5,14 19,22 12,17 5,22 7.5,14 1,9 9,9"/></svg>
        <span>Tobias Lindqvern and Elena K. Marwood</span>
        <svg viewBox="0 0 24 24" aria-hidden="true"><polygon fill="#d9262b" points="12,1 15,9 23,9 16.5,14 19,22 12,17 5,22 7.5,14 1,9 9,9"/></svg>
      </div>
      <div class="front-rule"></div>
    </section>
  </div>
</body>
</html>
```